Flyer for swimming pool service business

I am starting up a new pool cleaning business and I'm focusing on suburbs surrounding my suburb. So it will be a local service with fast, professional and friendly service.. I would like a Flyer of A5 size to drop into letterboxes local homes.

The business is called 'Gumtree Spa Care'

The following is what I would like in the flyer

Pool service frustrating you?
Troubled by poor water condition?
Tired of doing it yourself?

Keep your swimming pool sparkling and safe all year round

- water testing
- pool chemistry
- chlorine levels
- Ph balance
- equipment maintenance
- algae prevention
- leaf and debris maintenance
- filter cleaning
- tile cleaning
- salt water systems
- local service
- chemicals supplied and delivered
All for the low price of $40 a month (plus chemicals)

Relax and let Gumtree Spa Care take care of it for you.
for a one off service or a monthly service
no contracts

Contact details
Liam - 0417 382 604
gumtreespacare@westmail.net.au

Target Market(s)

the target market is a couples and familys 40-70 years old in a well off riverside suburb

Industry/Entity Type

Pool Service

Requirements
Must have
• Am looking to have a nice blue crystal clear water as part of the background either big or small.

Include my logo (provided) feel free to change the font of the Gumtree Spas Care writing on it, if that suits your design
Should not have
• cartoonish or funny images

```html
<!DOCTYPE html>
<html lang="en">
<head>
<meta charset="utf-8">
<title>Gumtree Spa Care – Flyer</title>
<link href="https://fonts.googleapis.com/css2?family=Montserrat:wght@600;700&family=Questrial&display=swap" rel="stylesheet">
<style>
  :root {
    --sky-deep: #2f6fc6;
    --sky-light: #8fbfe8;
    --sea: #1f5fae;
    --pool: #3fc3ee;
    --pool-light: #9fe2f8;
    --deck: #f4f7f8;
    --water-panel: #cfe7f7;
    --water-panel-light: #eef8fd;
    --navy: #1c3f93;
    --ink: #1e2430;
    --white: #ffffff;
  }
  * { margin: 0; padding: 0; box-sizing: border-box; }
  html, body { width: 1200px; height: 849px; overflow: hidden; background: var(--white); }
  .flyer {
    position: relative;
    width: 1200px;
    height: 849px;
    overflow: hidden;
    font-family: "Questrial", "Century Gothic", sans-serif;
  }
  .pool-photo {
    position: absolute;
    left: 0; top: 0;
    width: 829px; height: 849px;
    background:
      linear-gradient(180deg,
        var(--sky-deep) 0%,
        var(--sky-light) 46%,
        var(--sea) 49%,
        var(--sea) 53%,
        var(--deck) 55%,
        var(--pool) 62%,
        var(--pool-light) 88%,
        var(--deck) 100%);
  }
  .water-panel {
    position: absolute;
    left: 829px; top: 0;
    width: 371px; height: 849px;
    background:
      radial-gradient(ellipse at 70% 30%, var(--water-panel-light) 0%, transparent 60%),
      radial-gradient(ellipse at 20% 80%, var(--water-panel-light) 0%, transparent 55%),
      var(--water-panel);
  }
  .hero-copy {
    position: absolute;
    left: 48px; top: 60px;
    padding-left: 13px;
    border-left: 2px solid var(--white);
    color: var(--white);
  }
  .hero-questions {
    font-size: 18.5px;
    line-height: 24px;
  }
  .hero-headline {
    margin-top: 12px;
    font-family: "Montserrat", "Futura", sans-serif;
    font-weight: 700;
    font-size: 28.5px;
    line-height: 34px;
  }
  .offer {
    position: absolute;
    left: 862px; top: 54px;
    width: 320px;
    color: var(--ink);
  }
  .offer-price {
    font-family: "Montserrat", "Futura", sans-serif;
    font-weight: 700;
    font-size: 19.5px;
    line-height: 24px;
    color: var(--navy);
  }
  .offer-note {
    font-size: 15px;
    color: var(--navy);
    line-height: 20px;
  }
  .service-list {
    list-style: none;
    margin-top: 27px;
    font-size: 16px;
    line-height: 26.3px;
  }
  .service-list li::before { content: "• "; }
  .offer-pitch {
    margin-top: 20px;
    font-size: 16px;
    line-height: 24px;
  }
  .contact {
    margin-top: 25px;
    font-size: 16px;
    line-height: 24px;
  }
  .contact-detail {
    font-family: "Montserrat", "Futura", sans-serif;
    font-weight: 700;
    font-size: 16.5px;
    color: var(--navy);
    line-height: 25px;
  }
  .brand {
    position: absolute;
    left: 918px; top: 740px;
    display: flex;
    align-items: center;
    gap: 10px;
  }
  .brand-dot {
    width: 34px; height: 34px;
    border-radius: 50%;
    background: var(--navy);
  }
  .brand-name {
    font-family: "Montserrat", "Futura", sans-serif;
    font-weight: 700;
    font-size: 20px;
    color: var(--navy);
  }
</style>
</head>
<body>
<main class="flyer">
  <div class="pool-photo" role="img" aria-label="Photo of a sparkling blue resort swimming pool with palm trees, sun loungers and the sea under a clear sky"></div>
  <div class="water-panel" role="img" aria-label="Soft light blue rippling pool water texture"></div>

  <section class="hero-copy">
    <p class="hero-questions">Pool service frustrating you?<br>Troubled by poor water condition?<br>Tired of doing it yourself?</p>
    <h1 class="hero-headline">Keep your swimming pool<br>sparkling and safe all year round!</h1>
  </section>

  <section class="offer">
    <h2 class="offer-price">ALL FOR THE LOW PRICE<br>OF $40 A MONTH</h2>
    <p class="offer-note">(PLUS CHEMICALS)</p>
    <ul class="service-list">
      <li>Water Testing</li>
      <li>Pool Chemistry</li>
      <li>Chlorine Levels</li>
      <li>Ph Balance</li>
      <li>Equipment Maintenance</li>
      <li>Algae Prevention</li>
      <li>Leaf And Debris Maintenance</li>
      <li>Filter Cleaning</li>
      <li>Tile Cleaning</li>
      <li>Salt Water Systems</li>
      <li>Local Service</li>
      <li>Chemicals Supplied and Delivered</li>
    </ul>
    <p class="offer-pitch">Relax and let Gumtree Spa Care<br>take care of it for you. For a one off<br>service or a monthly service.<br>No contracts</p>
    <div class="contact">
      <p>Contact us:</p>
      <p class="contact-detail">0417 382 604 (Liam)</p>
      <p class="contact-detail">gumtreespacare@westmail.net.au</p>
    </div>
  </section>

  <div class="brand">
    <span class="brand-dot"></span>
    <span class="brand-name">Gumtree Spa Care</span>
  </div>
</main>
</body>
</html>
```